Holistic Psychology clinic flyer-

We need a 3 fold flyer that is both professional and zen looking with holistic elements- bilingual on both sides.
I am looking for a design that conveys the sense of confidence, yet relaxing to the eye and makes people want to pick it up and read it!
We are all about balance (yin, yang) and bringing equilibrium to a person in their quest to get better.

Target Market(s)

families adults, teens children experiencing mental health issues

Industry/Entity Type

Psychologist

Font styles to use
Serif

Colors
fbf289
cee9f5
0455a3

Requirements
Must have
• my logo (spiral) ; French one side; English on the other. Text is provided; Some color but clean, zen elements
• Easy to read text
Nice to have
• nature elements, bamboo? trees etc. sunrise or sunset?
• The sunset back ground provided in the picture is not necessary
• families?
Should not have
• too many distracting elements; not too many colors. colors must be subtle and must flow together

```html
<!DOCTYPE html>
<html lang="en">
<head>
<meta charset="utf-8">
<title>Equilibra – Trifold Flyer</title>
<link href="https://fonts.googleapis.com/css2?family=Playfair+Display:wght@400;700&family=Lora:ital,wght@0,400;0,500;1,400&family=Montserrat:wght@500;700&family=Roboto+Condensed:wght@700&display=swap" rel="stylesheet">
<style>
:root{
  --stage:#686c72;
  --navy:#27286b;
  --navy-deep:#1f2060;
  --gold:#e0ab2c;
  --ice:#edf6fb;
  --ink:#2b2b3a;
  --rule:#c9d3da;
  --white:#ffffff;
}
*{box-sizing:border-box;margin:0;padding:0}
html,body{width:1200px;height:2463px;overflow:hidden}
body{background:var(--stage);position:relative;font-family:"Lora",Georgia,serif;color:var(--ink)}
.flyer{position:absolute;left:30px;top:787px;width:1140px;height:888px;display:flex;box-shadow:0 10px 30px rgba(0,0,0,.35)}
.panel{position:relative;height:100%;overflow:hidden}

/* services panel */
.services{width:378px;background:var(--ice);padding:0 28px 0 28px}
.services__title{font-family:"Playfair Display",Georgia,serif;font-weight:400;font-size:22px;color:var(--navy);text-align:center;margin-top:88px}
.services__mark{display:block;width:20px;height:20px;border:3px solid var(--gold);border-radius:50%;margin:52px auto -78px}
.services__bar{width:46px;height:2px;background:var(--ink);margin:14px auto 22px}
.service{padding:12px 0 16px;border-bottom:1px solid var(--rule)}
.service:last-of-type{border-bottom:none}
.service h3{font-family:"Playfair Display",Georgia,serif;font-weight:400;font-size:15px;color:var(--ink);margin-bottom:3px}
.service p{font-size:10.6px;line-height:15.4px;text-align:justify}
.services__web{position:absolute;left:38px;bottom:0;width:296px;height:52px;background:var(--gold);border-radius:0 20px 0 0;color:var(--white);font-family:"Montserrat",Arial,sans-serif;font-weight:500;font-size:16px;display:flex;align-items:center;justify-content:center}

/* welcome panel */
.welcome{width:374px;background:var(--navy);color:var(--white);text-align:center}
.welcome__lead{font-family:"Playfair Display",Georgia,serif;font-size:22px;margin-top:40px}
.welcome__name{font-family:"Playfair Display",Georgia,serif;font-weight:700;font-size:34px;color:var(--gold);letter-spacing:1px;line-height:1}
.welcome__intro{font-size:10.6px;line-height:15.2px;text-align:justify;margin:26px 30px 0}
.welcome__tagline{font-family:"Playfair Display",Georgia,serif;font-size:25px;line-height:31px;margin-top:24px}
.welcome__tagline em{font-style:normal;color:var(--gold)}
.welcome__bio{font-size:10.6px;line-height:15.2px;text-align:justify;margin:26px 30px 0}
.welcome__bio strong{color:var(--gold);font-weight:500}
.welcome__base{position:absolute;left:0;bottom:0;width:374px;height:290px}
.contact-ring{position:absolute;left:86px;top:594px;width:202px;height:202px;border-radius:50%;background:var(--white);border:5px solid var(--gold);box-shadow:0 0 0 6px var(--white);color:var(--ink);font-family:"Roboto Condensed",Arial,sans-serif;font-weight:700;font-size:13.5px;line-height:19px;padding-top:26px}
.contact-ring__icons{display:flex;justify-content:center;gap:6px;margin-bottom:6px}
.contact-ring__icons svg{width:18px;height:18px}
.welcome__cta{position:absolute;left:0;right:0;top:818px;color:var(--navy);font-family:"Montserrat",Arial,sans-serif;font-weight:700;font-size:15.5px;line-height:20px}
.welcome__reach{position:absolute;left:0;right:0;top:862px;color:var(--gold);font-family:"Montserrat",Arial,sans-serif;font-weight:500;font-size:13.5px;display:flex;justify-content:center;align-items:center;gap:5px}
.welcome__reach svg{width:13px;height:13px}
.welcome__reach .sep{color:var(--navy)}

/* cover panel */
.cover{width:388px}
.cover__scene{position:absolute;inset:0;background:linear-gradient(180deg,#fbf7f1 0%,#f6e7d3 18%,#eebf7e 38%,#e59a3e 55%,#c46c1f 70%,#6b3a14 84%,#2a160a 100%)}
.cover__logo{position:absolute;top:66px;left:0;right:0;display:flex;align-items:center;justify-content:center;gap:12px;font-family:"Playfair Display",Georgia,serif;font-weight:400;font-size:52px;color:var(--navy)}
.cover__logo-dot{width:26px;height:26px;border-radius:50%;background:#f4e24a}
.cover__title{position:absolute;top:198px;left:0;right:0;text-align:center;font-family:"Playfair Display",Georgia,serif;font-weight:700;font-size:33px;line-height:41px;color:var(--navy)}
.cover__audience{position:absolute;bottom:22px;left:0;right:0;text-align:center;font-family:"Montserrat",Arial,sans-serif;font-weight:500;font-size:17px;color:var(--white)}
</style>
</head>
<body>
<main class="flyer">

  <section class="panel services">
    <span class="services__mark"></span>
    <h2 class="services__title">Our Professional Services</h2>
    <div class="services__bar"></div>

    <article class="service">
      <h3>Clinical Psychology</h3>
      <p>Psychologists are people specialists. Learn how to better understand both yourself and those in your life. Release some of the emotional and relational distress that drains you. It's time for change!</p>
    </article>
    <article class="service">
      <h3>Integrative Psychotherapy</h3>
      <p>We distill the very best approaches in psychology to help you free your mind, balance your body and heal your spirit. We specialize in helping you understand and harmonize the mind-body connection.</p>
    </article>
    <article class="service">
      <h3>Life Coaching</h3>
      <p>Life's challenges are opportunities for your growth. Our life coaches are skilled, caring and passionate about supporting you. Come in, it's time to discover your potential!</p>
    </article>
    <article class="service">
      <h3>Sports Psychology</h3>
      <p>There are many different psychological benefits of sports. Our sports psychologists can work with you to release your mental blocks, improve your performance and ensure success! Dare to aim high!</p>
    </article>
    <article class="service">
      <h3>Psycho-Educational Assessments</h3>
      <p>With the aid of psychometric tests, we can help you to figure out how your mind or that of your child works. We will highlight strengths and give recommendations to remedy any weaknesses. A detailed report and an academic intervention plan is customized for individuals aged 4-64!</p>
    </article>
    <article class="service">
      <h3>Mindfulness Meditation Classes</h3>
      <p>Meditation is much more than a relaxation technique. Mindfulness will bring you a heightened awareness and improved quality of life. These classes are offered weekly and will be useful to you to learn how to meditate and integrate it into your daily life. Find your inner peace!</p>
    </article>

    <div class="services__web">www.equilibra-clinic.com</div>
  </section>

  <section class="panel welcome">
    <p class="welcome__lead">Welcome to</p>
    <h1 class="welcome__name">EQUILIBRA</h1>
    <p class="welcome__intro">We present you with a whole new way of achieving wellness in your life. We offer a variety of clinical and educational services in a professional and peaceful environment. We use an integrative approach. We are delighted to present you with several effective and scientific approaches that can help you. We offer a variety of clinical and educational services in a professional and peaceful environment. We are committed to supporting you in reaching your potential and feeling better by adhering to an integrative mind-body approach. We are passionate about supporting you in reaching your potential and feeling well. It's time to start thinking of you...</p>
    <p class="welcome__tagline">Calm your <em>mind,</em><br><em>Relax</em> your body,<br>Nourish your <em>spirit.</em></p>
    <p class="welcome__bio"><strong>Mireille Tanguay, BSc, MA.</strong> is the founder and director of Equilibra. As a clinical psychologist, author and motivational speaker with 26 years of experience, Mireille is a pioneer in holistic psychology, an integrative approach that promotes healing and wellness. She and her staff are skilled in using cutting edge mind-body-spirit tools to help you with a variety of health, relational, educational and parenting issues. We look forward to supporting you and your family!</p>

    <svg class="welcome__base" viewBox="0 0 374 290" preserveAspectRatio="none" aria-hidden="true">
      <path d="M0 60 Q190 10 374 0 L374 290 L0 290 Z" fill="#ffffff"/>
      <path d="M0 52 Q190 2 374 -8" fill="none" stroke="#e0ab2c" stroke-width="4"/>
    </svg>

    <div class="contact-ring">
      <div class="contact-ring__icons">
        <svg viewBox="0 0 20 20"><circle cx="10" cy="10" r="10" fill="#27286b"/><path d="M10 4.5a3.6 3.6 0 0 0-3.6 3.6c0 2.7 3.6 7 3.6 7s3.6-4.3 3.6-7A3.6 3.6 0 0 0 10 4.5zm0 5a1.4 1.4 0 1 1 0-2.8 1.4 1.4 0 0 1 0 2.8z" fill="#fff"/></svg>
        <svg viewBox="0 0 20 20"><circle cx="10" cy="10" r="10" fill="#27286b"/><circle cx="10" cy="10" r="5.5" fill="none" stroke="#fff" stroke-width="1.2"/><path d="M4.5 10h11M10 4.5c-2.2 2.8-2.2 8.2 0 11M10 4.5c2.2 2.8 2.2 8.2 0 11" fill="none" stroke="#fff" stroke-width="1"/></svg>
      </div>
      4820 Lakeshore Rd ,<br>Beaconsfield,Québec<br>H9W 2K7<br>www.equilibra-clinic.com<br>www.social.com<br>/EquilibraClinic
    </div>

    <p class="welcome__cta">CONTACT US TODAY FOR A<br>FREE PHONE CONSULTATION</p>
    <p class="welcome__reach">
      <svg viewBox="0 0 14 14"><circle cx="7" cy="7" r="7" fill="#27286b"/><path d="M4.6 3.6l1.4 1.5-.7 1a5 5 0 0 0 2.6 2.6l1-.7 1.5 1.4-.9 1.1C6.8 10.4 3.6 7.2 3.5 4.5z" fill="#fff"/></svg>
      514-555-0142 <span class="sep">|</span>
      <svg viewBox="0 0 14 14"><circle cx="7" cy="7" r="7" fill="#27286b"/><rect x="3.5" y="4.6" width="7" height="4.8" rx=".6" fill="none" stroke="#fff" stroke-width="1"/><path d="M3.6 4.9L7 7.4l3.4-2.5" fill="none" stroke="#fff" stroke-width="1"/></svg>
      info@equilibra-clinic.com
    </p>
  </section>

  <section class="panel cover">
    <div class="cover__scene" role="img" aria-label="Photograph of a couple silhouetted against a golden sunset over a lake, one leaping into the other's arms"></div>
    <div class="cover__logo"><span class="cover__logo-dot"></span>Equilibra</div>
    <h2 class="cover__title">Psychologists<br>and Educational<br>Professionals<br>with an Integrative<br>Approach</h2>
    <p class="cover__audience">Children Teens Adults Couples</p>
  </section>

</main>
</body>
</html>
```